Powerpoint to present for client our social media services along with a test case

we need a powerpoint template design that is modern looking and eye catching and keeps the client engaged. we are a social media agency based in Kuwait so the content will be bilingual in english and in Arabic. i will be providing the logo and you can design based upon the logo provided. the main tasks for this PPT is to show case our case studies and for sales presentation. the presentations will be a mix of visuals, texts, graphs and charts.
the ppt design has to reflect the company colors in the logo with the logo scattered to show it is done by the company.

It Company

```html
<!DOCTYPE html>
<html lang="en">
<head>
<meta charset="utf-8">
<title>There are many variations</title>
<link href="https://fonts.googleapis.com/css2?family=Poppins:wght@600;700&family=Questrial&display=swap" rel="stylesheet">
<style>
  :root {
    --sidebar: #2d2a37;
    --magenta: #e2007f;
    --crimson: #a3103f;
    --lime: #8cc63f;
    --sky: #a3d2e2;
    --overlap: #8b1377;
    --ink: #111111;
    --body: #2a2a2a;
    --muted: #7a7a7a;
    --white: #ffffff;
  }
  * { margin: 0; padding: 0; box-sizing: border-box; }
  html, body { width: 1200px; height: 675px; overflow: hidden; background: #fff; }
  .slide {
    position: relative; width: 1200px; height: 675px; overflow: hidden;
    background: radial-gradient(ellipse at 55% 35%, #ffffff 0%, #f4f4f5 60%, #e9e9eb 100%);
    font-family: "Questrial", "Century Gothic", sans-serif; color: var(--body);
  }
  .shapes { position: absolute; inset: 0; width: 1200px; height: 675px; }
  .kicker {
    position: absolute; left: 146px; top: 44px;
    font-size: 12.5px; letter-spacing: 0.2px; color: var(--muted); text-transform: uppercase;
  }
  .title {
    position: absolute; left: 144px; top: 62px;
    font-family: "Poppins", "Century Gothic", sans-serif; font-weight: 700;
    font-size: 41px; letter-spacing: -0.5px; color: var(--ink);
  }
  .lead {
    position: absolute; left: 146px; top: 186px; width: 540px;
    list-style: none; font-family: "Poppins", sans-serif; font-weight: 600;
    font-size: 16.5px; line-height: 26px; color: var(--ink);
  }
  .lead li { position: relative; padding-left: 22px; }
  .lead li::before {
    content: ""; position: absolute; left: 2px; top: 10px; width: 7px; height: 7px; background: var(--ink);
  }
  .points {
    position: absolute; left: 194px; top: 248px; list-style: none;
    font-size: 16.5px; line-height: 23px; color: var(--body);
  }
  .points li { position: relative; padding-left: 18px; }
  .points li::before {
    content: ""; position: absolute; left: 0; top: 10px; width: 5px; height: 5px; background: var(--ink);
  }
  .body-copy {
    position: absolute; left: 191px; top: 366px; width: 460px;
    font-size: 17.5px; line-height: 24.5px; text-align: justify; color: var(--body);
  }
  .callout {
    position: absolute; left: 812px; top: 264px; width: 360px;
    font-family: "Poppins", sans-serif; font-weight: 600;
    font-size: 23px; line-height: 32.5px; color: var(--white); white-space: nowrap;
  }
  .footer-meta {
    position: absolute; right: 106px; top: 605px; text-align: right; color: var(--muted);
    font-size: 14px; line-height: 16px;
  }
  .footer-meta .date { font-family: "Poppins", sans-serif; font-weight: 600; font-size: 13.5px; color: #5c5c5c; }
  .divider { position: absolute; left: 1108px; top: 604px; width: 1px; height: 40px; background: #9a9a9a; }
  .page-number {
    position: absolute; left: 1120px; top: 598px;
    font-family: "Poppins", sans-serif; font-weight: 700; font-size: 32px; color: #555;
  }
  .brand {
    position: absolute; left: 33px; top: 655px;
    transform: rotate(-90deg); transform-origin: left top;
    display: flex; align-items: center; gap: 8px;
    font-family: "Poppins", sans-serif; font-weight: 700; font-size: 15px;
    letter-spacing: 2px; color: var(--white); white-space: nowrap;
  }
  .brand .dot { width: 14px; height: 14px; border-radius: 50%; background: var(--magenta); }
</style>
</head>
<body>
<div class="slide">
  <svg class="shapes" viewBox="0 0 960 540" aria-hidden="true">
    <rect class="sidebar" x="0" y="0" width="52" height="540" fill="var(--sidebar)"/>
    <polygon points="0,0 95,0 52,27 0,58" fill="var(--magenta)"/>
    <polygon points="0,14 52,27 0,58" fill="var(--crimson)"/>
    <polygon points="18,58 62,24 62,90" fill="var(--lime)"/>
    <polygon points="712,152 960,20 960,540 712,540" fill="var(--sky)"/>
    <polygon points="585,138 760,182 760,310 585,350" fill="var(--magenta)"/>
    <polygon points="712,170 760,182 760,310 712,321" fill="var(--overlap)"/>
  </svg>

  <div class="kicker">Building brands through communities</div>
  <h1 class="title">There are many variations</h1>

  <ul class="lead">
    <li>Web visits to mobile sites forecast to overtake desktop access by 2014</li>
  </ul>
  <ul class="points">
    <li>Create a strategy for the entire Share service</li>
    <li>Divide Corvia Portal into solutions business users can relate to</li>
    <li>Establish a common communication platform</li>
  </ul>

  <p class="body-copy">There are many variations of passages of Lorem Ipsum available, but the majority have suffered alteration in some form, by injected humour, or randomised words which don't look even slightly believable. If you are going to use a passage of Lorem Ipsum, you need to be sure there isn't anything embarrassing hidden in the middle of text.</p>

  <p class="callout">It is a long established fact<br>that a reader will be dis-<br>tracted by the readable</p>

  <div class="footer-meta">
    <div class="date">March 24, 2014</div>
    <div class="url">www.sahelmedia.com</div>
  </div>
  <div class="divider"></div>
  <div class="page-number">2</div>

  <div class="brand"><span class="dot"></span>SAHEL MEDIA</div>
</div>
</body>
</html>
```